BrightLedgerMoney(.com) needs website & logo design

We need our website mock-up made into a reality! We are wanting to launch a multifaceted website for all things financial - i.e. blogs, financial wellness information, and a network of redirect links.
We have an existing mock-up, which I will include, but are open to your creative approach!

Industry/Entity Type

Finance

Coding

Coded - Design and coding required

Number of Pages Required

1 page

Requirements
Must have
• Corresponding logo

```html
<!DOCTYPE html>
<html lang="en">
<head>
<meta charset="utf-8">
<title>Bright Ledger Money</title>
<link href="https://fonts.googleapis.com/css2?family=Poppins:wght@400;500;600;700&display=swap" rel="stylesheet">
<style>
:root{
  --teal:#74d8bf;
  --teal-dark:#3fb597;
  --ink:#1e1e1e;
  --body:#555;
  --charcoal:#333333;
  --footer:#1b1b1b;
  --white:#ffffff;
}
*{margin:0;padding:0;box-sizing:border-box}
html,body{width:1200px;height:4239px;overflow:hidden}
body{position:relative;font-family:'Poppins',sans-serif;color:var(--ink);background:var(--white)}
.abs{position:absolute}
svg.icon{fill:none;stroke:var(--ink);stroke-width:2.2;stroke-linecap:round;stroke-linejoin:round}

/* header */
.site-header{left:0;top:0;width:1200px;height:79px;background:var(--white);border-top:2px solid var(--teal);z-index:5}
.brand{left:110px;top:14px;font-weight:700;font-size:22px;line-height:24px;color:var(--ink);text-align:center}
.nav{left:0;top:32px;font-size:15px;color:var(--ink)}
.nav a{position:absolute;white-space:nowrap;text-decoration:none;color:inherit}
.nav a.active{color:var(--teal-dark);border-bottom:2px solid var(--teal);padding-bottom:3px}
.btn{display:flex;align-items:center;justify-content:center;background:var(--teal);border:3px solid #5cc4aa;border-radius:30px;font-size:12px;font-weight:600;letter-spacing:.5px;color:var(--ink);box-shadow:0 2px 4px rgba(0,0,0,.2)}

/* hero */
.hero-photo{left:0;top:79px;width:1200px;height:632px;background:linear-gradient(100deg,#6d5a4a 0%,#b9a58f 25%,#8a7c70 45%,#4a4440 65%,#2d2a28 85%,#8a6c52 100%)}
.hero-panel{left:566px;top:196px;width:634px;height:347px;background:rgba(22,22,22,.82)}
.hero-title{left:637px;top:222px;font-size:52px;font-weight:700;line-height:65px;color:var(--white)}
.hero-title span{color:var(--teal)}
.hero-sub{left:637px;top:436px;width:500px;font-size:19px;font-weight:500;line-height:31px;color:var(--white)}

.signup{left:181px;top:622px;width:821px;height:227px;background:var(--white);border-radius:6px;box-shadow:0 6px 18px rgba(0,0,0,.15)}
.signup h2{position:absolute;left:0;top:26px;width:100%;text-align:center;font-size:31px;font-weight:500;letter-spacing:.5px}
.email-field{position:absolute;left:107px;top:96px;width:609px;height:41px;border:2px solid #aaa;border-radius:22px;font-size:14px;padding:10px 34px}
.signup .btn{position:absolute;left:339px;top:153px;width:145px;height:41px}

/* feature strip */
.strip{left:0;top:894px;width:1200px;height:187px;display:flex;border-top:1px solid #ddd;border-bottom:1px solid #ddd}
.strip-item{width:200px;height:100%;display:flex;flex-direction:column;align-items:center;padding-top:38px;font-size:17px;font-weight:500;border-right:1px solid #ddd}
.strip-item.teal{background:var(--teal)}
.strip-item svg{width:62px;height:62px;margin-bottom:28px}

/* trending */
.frame-teal{left:110px;top:1185px;width:250px;height:420px;background:var(--teal)}
.trend-photo{left:148px;top:1203px;width:436px;height:385px;background:linear-gradient(160deg,#d8d6d0 0%,#9aa3a6 40%,#3c8fa0 70%,#e3c84a 100%)}
.section-heading{font-size:34px;font-weight:500;line-height:41px;color:var(--ink);letter-spacing:.3px}
.section-heading .accent{color:var(--teal);font-weight:700}
.rule{height:3px;width:62px;background:var(--teal)}
.copy{font-size:14.5px;line-height:25px;color:var(--body)}
.trend-copy{left:614px;top:1313px;width:480px;letter-spacing:-.1px}
.trend-copy p+p{margin-top:16px}

/* topics */
.topics{left:0;top:1692px;width:1200px;height:721px;background:var(--charcoal)}
.topic{width:300px;height:255px;background:var(--teal);display:flex;flex-direction:column;align-items:center;padding-top:50px;font-size:23px;font-weight:600}
.topic svg{width:100px;height:100px;margin-bottom:30px}

/* wellness */
.well-dark{left:851px;top:2482px;width:250px;height:420px;background:#2b2b2b}
.well-photo{left:627px;top:2500px;width:436px;height:385px;background:linear-gradient(110deg,#cfcac2 0%,#a87a55 35%,#7a3a2a 55%,#2f3a45 75%,#1d2830 100%)}

/* blog */
.blog{left:0;top:2991px;width:1200px;height:571px;background:var(--teal)}
.blog-card{top:174px;width:305px;height:310px;overflow:hidden}
.blog-card .shade{position:absolute;left:0;bottom:0;width:100%;height:130px;background:linear-gradient(rgba(0,0,0,0),rgba(0,0,0,.85))}
.blog-card .date{position:absolute;left:10px;top:215px;width:285px;font-size:13px;color:var(--white);padding-bottom:10px;border-bottom:1px solid rgba(255,255,255,.7)}
.blog-card .title{position:absolute;left:10px;top:251px;width:290px;font-size:14px;font-weight:500;line-height:21px;color:var(--white)}
.blog-card.faded{opacity:.45}
.arrow-btn{width:48px;height:48px;border-radius:50%;background:var(--white);display:flex;align-items:center;justify-content:center}

/* questions */
.questions h2{left:0;top:3638px;width:1200px;text-align:center;font-size:36px;font-weight:500;letter-spacing:.5px}
.questions p{left:160px;top:3722px;width:880px;text-align:center}

/* footer */
.site-footer{left:0;top:3949px;width:1200px;height:290px;background:var(--footer);color:var(--white)}
.foot-brand{left:178px;top:58px;width:220px;text-align:center;font-size:30px;font-weight:700;line-height:36px}
.social{top:153px;width:30px;height:30px;border-radius:50%;background:#3a3a3a;border:1px solid #555}
.foot-title{top:50px;font-size:17px;font-weight:500}
.foot-rule{top:84px;width:50px;height:2px;background:var(--teal)}
.foot-link{font-size:12px;font-weight:500}
.contact-dot{width:34px;height:34px;border-radius:50%;background:#3a3a3a;display:flex;align-items:center;justify-content:center}
.contact-text{font-size:13px;line-height:18px}
.foot-divider{left:110px;top:219px;width:978px;height:1px;background:var(--teal)}
.copyright{left:0;top:241px;width:1200px;text-align:center;font-size:13px}
</style>
</head>
<body>

<header class="abs site-header">
  <div class="abs brand">Bright Ledger<br>Money</div>
  <nav class="abs nav">
    <a class="active" style="left:472px">Home</a>
    <a style="left:556px">About</a>
    <a style="left:642px">Services</a>
    <a style="left:744px">Blog</a>
    <a style="left:818px">Testimonials</a>
  </nav>
  <div class="abs btn" style="left:942px;top:20px;width:146px;height:42px">CONTACT US</div>
</header>

<section class="hero">
  <div class="abs hero-photo" role="img" aria-label="Two colleagues reviewing financial papers and a tablet in an office"></div>
  <div class="abs hero-panel"></div>
  <h1 class="abs hero-title">A CLEAR PATH<br>TO <span>FINANCIAL</span><br><span>WELLNESS</span></h1>
  <p class="abs hero-sub">Having insight to relevant information is what we bring to you in a clear and easy to digest way.</p>
  <div class="abs signup">
    <h2>SIGNUP FOR FREE</h2>
    <div class="email-field">Your Email</div>
    <div class="btn">GET STARTED</div>
  </div>
</section>

<section class="abs strip">
  <div class="strip-item teal"><svg class="icon" viewBox="0 0 60 60"><rect x="8" y="8" width="44" height="44" rx="6"/><rect x="18" y="8" width="22" height="14"/><rect x="16" y="34" width="28" height="18"/></svg>Save</div>
  <div class="strip-item"><svg class="icon" viewBox="0 0 60 60"><path d="M26 12a20 20 0 1 0 20 20H26z"/><path d="M32 6v20h20A20 20 0 0 0 32 6z"/><path d="M6 40h14M12 34h10"/></svg>Budget</div>
  <div class="strip-item teal"><svg class="icon" viewBox="0 0 60 60"><ellipse cx="30" cy="30" rx="24" ry="9"/><ellipse cx="30" cy="30" rx="24" ry="9" transform="rotate(60 30 30)"/><ellipse cx="30" cy="30" rx="24" ry="9" transform="rotate(120 30 30)"/><circle cx="30" cy="30" r="3"/></svg>Calculate</div>
  <div class="strip-item"><svg class="icon" viewBox="0 0 60 60"><circle cx="48" cy="12" r="7"/><circle cx="30" cy="34" r="4"/><circle cx="10" cy="50" r="4"/><path d="M13 48l14-12M33 32l10-14"/></svg>Track</div>
  <div class="strip-item teal"><svg class="icon" viewBox="0 0 60 60"><circle cx="26" cy="26" r="14"/><path d="M36 36l16 16"/><circle cx="26" cy="26" r="6"/><path d="M44 6v6M50 12h-6"/></svg>Research</div>
  <div class="strip-item"><svg class="icon" viewBox="0 0 60 60"><path d="M6 54h50"/><rect x="10" y="40" width="8" height="14"/><rect x="24" y="32" width="8" height="22"/><rect x="38" y="22" width="8" height="32"/><path d="M8 30L28 12l8 6 14-12"/></svg>Invest</div>
</section>

<section class="trending">
  <div class="abs frame-teal"></div>
  <div class="abs trend-photo" role="img" aria-label="Group of people meeting in a bright modern lounge"></div>
  <h2 class="abs section-heading" style="left:614px;top:1196px">TRENDING IN 2021:<br><span class="accent">FINANCIAL LITERACY</span></h2>
  <div class="abs rule" style="left:614px;top:1293px"></div>
  <div class="abs copy trend-copy">
    <p>Saerspiciatis undeasepoiise osamnis istasesee njhhjkatus error sit voluptatem accusan tium doloreasmque laudantium, totam rem aperiam, ease aque ipaefdsa quae ab illo inventore veritatis ease quasi architecto beatae vitae diascta sunt explicabo. Nemo enim ipsam voluptatem quia volupta sde sessitasese aspernatur autodit aut fugitsdsed quia conseq aauuntur magni dolores eos qui ratione voluptatem sequi nesciunt.</p>
    <p>Dseste natus error sit voluptatem accusan tium doloremque laudantium, totam rem aperiam, ease aque ipaefdsa quae ab illo inventore veritatis ease quasi architecto.</p>
  </div>
</section>

<section class="abs topics">
  <div class="abs topic" style="left:110px;top:86px"><svg class="icon" viewBox="0 0 100 100"><circle cx="50" cy="50" r="30"/><circle cx="50" cy="50" r="20"/><path d="M50 8v20M50 72v20M8 50h20M72 50h20"/><path d="M42 58v-6M48 58v-10M54 58v-14M40 48l8-6 4 3 8-7"/></svg>Set Goals</div>
  <div class="abs topic" style="left:449px;top:86px"><svg class="icon" viewBox="0 0 100 100"><circle cx="42" cy="40" r="28"/><circle cx="42" cy="40" r="19"/><path d="M62 60l8 8"/><rect x="66" y="64" width="10" height="26" rx="4" transform="rotate(-45 71 77)"/><path d="M48 32c-2-4-12-4-12 2s12 4 12 10-10 6-12 2M42 26v30"/></svg>Money 101</div>
  <div class="abs topic" style="left:788px;top:86px"><svg class="icon" viewBox="0 0 100 100"><circle cx="50" cy="28" r="16"/><path d="M55 22c-2-3-10-3-10 1s10 3 10 8-8 5-10 1M50 18v22"/><path d="M10 62l16-4 18 6h14a5 5 0 0 1 0 10H40"/><path d="M58 70l20-10a5 5 0 0 1 6 8L60 84H30l-12-6"/><path d="M84 56v34"/></svg>Budgeting</div>
  <div class="abs topic" style="left:110px;top:377px"><svg class="icon" viewBox="0 0 100 100"><path d="M60 90V74h10a6 6 0 0 0 6-6V58l8-4-8-12c0-18-14-32-32-32S14 24 14 42c0 12 6 20 12 26v22"/><circle cx="50" cy="40" r="8"/><circle cx="50" cy="40" r="16" stroke-dasharray="6 5"/></svg>Credit Mindfulness</div>
  <div class="abs topic" style="left:449px;top:377px"><svg class="icon" viewBox="0 0 100 100"><circle cx="50" cy="44" r="30" stroke-dasharray="10 6"/><circle cx="50" cy="40" r="7"/><circle cx="34" cy="52" r="5"/><circle cx="66" cy="52" r="5"/><path d="M38 78v-16a12 12 0 0 1 24 0v16M22 78V68a8 8 0 0 1 12-6M78 78V68a8 8 0 0 0-12-6"/><path d="M16 82h68"/></svg>Debt Management</div>
  <div class="abs topic" style="left:788px;top:377px"><svg class="icon" viewBox="0 0 100 100"><path d="M30 14l10 36h26l6 20M40 50l-8 26M66 50l-4 12"/><path d="M14 70c20 16 52 18 74 6"/><path d="M48 44h20"/></svg>Retirement Planning</div>
</section>

<section class="wellness">
  <h2 class="abs section-heading" style="left:153px;top:2588px">FINANCIAL <span class="accent">WELLNESS 101</span></h2>
  <div class="abs rule" style="left:526px;top:2649px"></div>
  <p class="abs copy" style="left:112px;top:2670px;width:476px;text-align:right">Saerspiciatis undeasepoiise osamnis istasesee njhhjkatus error sit voluptatem accusan tium doloreasmque laudantium, totam rem aperiam, ease aque ipaefdsa quae ab illo inventore veritatis ease quasi architecto beatae vitae diascta sunt.</p>
  <div class="abs well-dark"></div>
  <div class="abs well-photo" role="img" aria-label="Two colleagues discussing analysis charts on a glass board"></div>
</section>

<section class="abs blog">
  <h2 class="abs section-heading" style="left:0;top:79px;width:1200px;text-align:center">OUR <b>BLOG</b></h2>
  <div class="abs" style="left:569px;top:140px;width:62px;height:3px;background:var(--ink)"></div>
  <div class="abs blog-card faded" style="left:-234px;background:linear-gradient(135deg,#6a8f5a,#2d4a34)" role="img" aria-label="Blog post photo"><div class="shade"></div><div class="date">March 20, 2023</div><div class="title">Voluptatem Eccusantium Soloremque laudantium</div></div>
  <div class="abs blog-card" style="left:107px;background:linear-gradient(135deg,#9b8f85,#5a4538 60%,#2b2522)" role="img" aria-label="Person working on a laptop with charts"><div class="shade"></div><div class="date">March 20, 2023</div><div class="title">Voluptatem Eccusantium Soloremque laudantium</div></div>
  <div class="abs blog-card" style="left:446px;background:linear-gradient(135deg,#3a5a78,#7c8a92 50%,#2a2a2a)" role="img" aria-label="Desk with financial reports and a monitor"><div class="shade"></div><div class="date">March 20, 2023</div><div class="title">Voluptatem Eccusantium Soloremque laudantium</div></div>
  <div class="abs blog-card" style="left:787px;background:linear-gradient(135deg,#1a2640,#4a5a80 55%,#c98a3a)" role="img" aria-label="Line chart of market data"><div class="shade"></div><div class="date">March 20, 2023</div><div class="title">Voluptatem Eccusantium Soloremque laudantium</div></div>
  <div class="abs blog-card faded" style="left:1126px;background:linear-gradient(135deg,#6a8f5a,#2d4a34)" role="img" aria-label="Blog post photo"><div class="shade"></div><div class="date">March 20, 2023</div><div class="title">Voluptatem Eccusantium Soloremque laudantium</div></div>
  <div class="abs arrow-btn" style="left:29px;top:305px"><svg class="icon" width="20" height="20" viewBox="0 0 20 20" style="stroke:var(--teal-dark)"><path d="M16 10H4M9 5l-5 5 5 5"/></svg></div>
  <div class="abs arrow-btn" style="left:1122px;top:305px"><svg class="icon" width="20" height="20" viewBox="0 0 20 20" style="stroke:var(--teal-dark)"><path d="M4 10h12M11 5l5 5-5 5"/></svg></div>
</section>

<section class="questions">
  <h2 class="abs">HAVE ANY QUESTIONS?</h2>
  <p class="abs copy">Saerspiciatis undeasepoiise osamnis istasesee njhhjkatus erreror sisaght voluptatem accudrsan tium doloreasmque laudantium, totam rem aperiam, ease aque ipaefdsa quae ab illo inventore veritatis ease quasi architecto beatae vitae diascta sunt.</p>
  <div class="abs btn" style="left:527px;top:3821px;width:146px;height:41px">CONTACT US</div>
</section>

<footer class="abs site-footer">
  <div class="abs foot-brand">Bright Ledger<br>Money</div>
  <div class="abs social" style="left:197px"></div>
  <div class="abs social" style="left:242px"></div>
  <div class="abs social" style="left:286px"></div>
  <div class="abs social" style="left:331px"></div>
  <div class="abs social" style="left:375px"></div>

  <div class="abs foot-title" style="left:515px">LATEST POSTS</div>
  <div class="abs foot-rule" style="left:515px"></div>
  <div class="abs foot-link" style="left:515px;top:117px">Hello world!</div>
  <div class="abs foot-link" style="left:515px;top:153px">Successful Marketing Ads for Your</div>

  <div class="abs foot-title" style="left:820px">CONTACT US</div>
  <div class="abs foot-rule" style="left:820px"></div>
  <div class="abs contact-dot" style="left:821px;top:100px"><svg width="16" height="16" viewBox="0 0 24 24" fill="var(--teal)"><path d="M6.6 10.8a15 15 0 0 0 6.6 6.6l2.2-2.2a1 1 0 0 1 1-.25 11.4 11.4 0 0 0 3.6.57 1 1 0 0 1 1 1V20a1 1 0 0 1-1 1A17 17 0 0 1 3 4a1 1 0 0 1 1-1h3.5a1 1 0 0 1 1 1c0 1.25.2 2.45.57 3.6a1 1 0 0 1-.25 1z"/></svg></div>
  <div class="abs contact-text" style="left:872px;top:99px">Call Us:<br>+1 (555) 014-2290</div>
  <div class="abs contact-dot" style="left:821px;top:157px"><svg width="16" height="16" viewBox="0 0 24 24" fill="var(--teal)"><path d="M3 5h18a1 1 0 0 1 1 1v12a1 1 0 0 1-1 1H3a1 1 0 0 1-1-1V6a1 1 0 0 1 1-1zm1 2v.5l8 5 8-5V7z"/></svg></div>
  <div class="abs contact-text" style="left:872px;top:156px">Email:<br>hello@brightledgermoney.com</div>

  <div class="abs foot-divider"></div>
  <div class="abs copyright">©2023. All rights reserved.</div>
</footer>

</body>
</html>
```